Seriöses Webdesign für innovatives Ingenieurbüro mit dem Schwerpunkt Eisenbahn Leit- und Sicherungstechnik
Zielgruppe
Die Webseite hat in erster Linie die Aufgabe zu informieren: An erster Stelle steht die Kontaktaufnahme und der Kompetenzbereich des Ingenieurbüros.
Folgende Kernkompetenzen sollen durch die Webseite transportiert werden:
Hardware-Entwicklung
Software-Entwicklung
Erneuerung alter Techniken
Begutachtung
Software für Lieferantenbewertung
Störungsmanagement(system)
Zielgruppe:
Die Webseite soll als Online-Visitenkarte für bestehende und neue Kontakte dienen. Gerade neue (Messe-)Kontakte erleben die Webseite als erste Anlaufstelle und erhalten einen Einblick in das vorhandene Leistungsspektrum des Ingenieurbüros und die Möglichkeiten der Kontaktaufnahme.

```html
<!DOCTYPE html>
<html lang="de">
<head>
<meta charset="utf-8">
<title>Vektra Consult – Ingenieurbüro</title>
<link rel="stylesheet" href="https://fonts.googleapis.com/css2?family=Arimo:wght@400;600;700&display=swap">
<style>
  :root {
    --brand: #7ccbea;
    --rule: #9fd6ec;
    --text: #555555;
    --text-soft: #5e5e5e;
    --panel: #e1e1e1;
    --menu-rule: #7c9ba2;
    --bg: #ffffff;
  }
  * { margin: 0; padding: 0; box-sizing: border-box; }
  html, body { width: 1200px; height: 767px; overflow: hidden; background: var(--bg); }
  body { position: relative; font-family: "Arimo", Helvetica, Arial, sans-serif; color: var(--text); }

  .site-header { position: absolute; left: 0; top: 0; width: 1200px; height: 72px; border-bottom: 1px solid var(--rule); }
  .brand { position: absolute; left: 226px; top: 26px; font-size: 31px; font-weight: 700; color: var(--brand); line-height: 34px; letter-spacing: 0.5px; }
  .contact { position: absolute; top: 43px; font-size: 14.6px; line-height: 16px; color: var(--text-soft); }
  .contact-mail { left: 746px; }
  .contact-phone { left: 898px; display: flex; align-items: center; gap: 3px; }
  .contact-phone svg { width: 10px; height: 14px; }

  .side-panel { position: absolute; left: 198px; top: 84px; width: 300px; height: 635px; background: var(--panel); }
  .service-nav { position: absolute; left: 227px; top: 115px; width: 234px; list-style: none; }
  .service-nav li { height: 33px; padding-top: 12px; border-bottom: 1px solid var(--menu-rule); font-size: 13px; line-height: 13px; font-weight: 600; color: var(--text); }

  .hero { position: absolute; left: 498px; top: 85px; width: 504px; height: 150px;
    background: linear-gradient(160deg, #6d6a68 0%, #8b8886 35%, #c9c9c9 55%, #7a7573 75%, #5c5654 100%); }

  .content { position: absolute; left: 574px; top: 309px; width: 440px; }
  .content h1 { font-size: 21px; line-height: 22px; font-weight: 600; color: var(--brand); }
  .lead { position: absolute; top: 34.6px; width: 440px; font-size: 15.2px; line-height: 24.5px; font-weight: 700; color: var(--text); }
  .body-text { position: absolute; width: 440px; font-size: 12.4px; line-height: 24.5px; color: var(--text-soft); }
  .body-one { top: 133.7px; }
  .body-two { top: 232.8px; }

  .site-footer { position: absolute; left: 0; top: 731px; width: 1200px; height: 36px; border-top: 1px solid var(--rule); }
  .footer-link { position: absolute; top: 8px; font-size: 13px; line-height: 14px; font-weight: 600; color: #666666; }
</style>
</head>
<body>
  <header class="site-header">
    <div class="brand">Vektra Consult</div>
    <div class="contact contact-mail">info@vektra-consult.de</div>
    <div class="contact contact-phone">
      <svg viewBox="0 0 10 14" aria-hidden="true"><path d="M6 0.5 C2.5 1.5 1 4.5 1 7 C1 9.5 2.5 12.5 6 13.5 L7 10.5 L5 9.5 C4.3 8.5 4.3 5.5 5 4.5 L7 3.5 Z" fill="#666"/></svg>
      <span>0152 00 41 93</span>
    </div>
  </header>

  <aside class="side-panel" role="img" aria-label="Helle Fläche mit geprägtem Gleisplan-Muster"></aside>
  <ul class="service-nav">
    <li>Hardware-Entwicklung</li>
    <li>Software-Entwicklung</li>
    <li>Erneuerung alter Techniken</li>
    <li>Begutachtung</li>
    <li>Software für Lieferantenbewertung</li>
    <li>Störungsmanagement(system)</li>
  </ul>

  <div class="hero" role="img" aria-label="Foto eines Hochgeschwindigkeitszugs auf mehrgleisiger Strecke mit Oberleitung"></div>

  <main class="content">
    <h1>Dies ist ein Typoblindtext</h1>
    <p class="lead">An ihm kann man sehen, ob alle Buchstaben da sind und<br>wie sie aussehen. Manchmal benutzt man Worte wie<br>Hamburgefonts, oder Handgloves, um Schriften zu testen.</p>
    <p class="body-text body-one">Manchmal Sätze, die alle Buchstaben des Alphabets enthalten -<br>man nennt diese Sätze »Pangrams«. Sehr bekannt ist dieser:<br>The quick brown fox jumps over the lazy old dog.</p>
    <p class="body-text body-two">Oft werden in Typoblindtexte auch fremdsprachige Satzteile eingebaut<br>(ARVEL® and Nelox™ are testing aussi la Kerning), um die Wirkung in<br>anderen Sprachen zu testen.</p>
  </main>

  <footer class="site-footer">
    <span class="footer-link" style="left:500px">Impressum</span>
    <span class="footer-link" style="left:610px">Datenschutz</span>
    <span class="footer-link" style="left:730px">Hilfe</span>
    <span class="footer-link" style="left:800px">Copyright</span>
    <span class="footer-link" style="left:903px">Sprache ändern</span>
  </footer>
</body>
</html>
```